Personal Training

The name of my company is Heron Fitness. I am looking for a design that will feature the 8 components I am utilizing in my workouts (strength, flexibility, agility, core, power, balance, cardiovacular, speed) and represent the spider. It is not essesstial to have a spider for my logo but would be nice. If a spider is used please do not use a logo like Gullwoman, a tarantula, or anything scary involving a spider (I have female clients who would get scared) lol
If you need me to provide more information please let me know. Feel free to check my website for ideas but ignore the pictures on my site as those are not pictures of me or clients
Thank you in advance!

Industry/Entity Type

Fitness

Contact Information for Business Card

Mark Delaney
Company Name: Heron Fitness
Tag line: 8 components to a better you
Website: hernfit4.example
Email: mark@hernfit4.example
Cell: 555-314-2086

CQBL Certified Personal Trainer
CPR AED National Pulse Federation
B.A. Exercise Physiology W.K.R., 2004

```html
<!DOCTYPE html>
<html lang="en">
<head>
<meta charset="utf-8">
<title>Heron Fitness – Business Card</title>
<link rel="stylesheet" href="https://fonts.googleapis.com/css2?family=Michroma&family=Oswald:wght@500&family=Open+Sans:wght@400;600;700&display=swap">
<style>
  :root {
    --page-bg: #ffffff;
    --silver-top: #a9a9ab;
    --silver-mid: #d8d8da;
    --silver-low: #f1f1f2;
    --brand-red: #e01f26;
    --band-red: #b8141b;
    --card-black: #111112;
    --card-black-soft: #1d1d1f;
    --ink-dark: #141414;
    --text-light: #f4f4f4;
  }
  * { margin: 0; padding: 0; box-sizing: border-box; }
  html, body {
    width: 1200px;
    height: 900px;
    overflow: hidden;
    background: var(--page-bg);
  }
  .business-card {
    position: absolute;
    left: 100px;
    top: 165px;
    width: 1000px;
    height: 570px;
    border-radius: 38px;
    overflow: hidden;
    background: var(--card-black);
    font-family: "Open Sans", Arial, sans-serif;
  }
  .card-header {
    position: absolute;
    inset: 0 0 auto 0;
    height: 258px;
    background: linear-gradient(180deg, var(--silver-top) 0%, var(--silver-mid) 45%, var(--silver-low) 100%);
  }
  .brand-mark {
    position: absolute;
    left: 58px;
    top: 78px;
    width: 160px;
    height: 160px;
    border-radius: 22px;
    background: var(--brand-red);
    border: 4px solid var(--ink-dark);
  }
  .brand-name {
    position: absolute;
    left: 250px;
    top: 112px;
    font-family: "Michroma", Arial, sans-serif;
    font-size: 50px;
    letter-spacing: 1px;
    color: var(--brand-red);
    text-transform: uppercase;
    line-height: 1;
  }
  .brand-tagline {
    position: absolute;
    left: 250px;
    top: 187px;
    font-family: "Michroma", Arial, sans-serif;
    font-size: 21px;
    letter-spacing: 3px;
    color: var(--ink-dark);
    text-transform: uppercase;
    line-height: 1;
  }
  .components-band {
    position: absolute;
    left: 0;
    top: 258px;
    width: 100%;
    height: 30px;
    background: var(--band-red);
    color: var(--ink-dark);
    font-family: "Oswald", Arial, sans-serif;
    font-weight: 500;
    font-size: 17px;
    letter-spacing: 3.2px;
    text-transform: uppercase;
    line-height: 30px;
    padding-left: 58px;
    white-space: nowrap;
  }
  .card-body {
    position: absolute;
    left: 0;
    top: 288px;
    width: 100%;
    bottom: 0;
    background:
      radial-gradient(circle, var(--card-black-soft) 1px, transparent 1.5px) 0 0 / 6px 6px,
      var(--card-black);
  }
  .trainer-name {
    position: absolute;
    left: 58px;
    top: 22px;
    font-size: 30px;
    font-weight: 700;
    color: var(--brand-red);
  }
  .credentials {
    position: absolute;
    left: 58px;
    top: 68px;
    list-style: none;
    font-size: 18px;
    line-height: 25px;
    color: var(--text-light);
  }
  .contact-list {
    position: absolute;
    left: 58px;
    top: 158px;
    list-style: none;
    font-size: 27px;
    line-height: 40px;
    color: var(--text-light);
  }
  .contact-list li {
    display: flex;
    align-items: center;
    gap: 10px;
  }
  .contact-icon {
    width: 28px;
    height: 28px;
    flex: none;
  }
</style>
</head>
<body>
  <article class="business-card">
    <header class="card-header">
      <div class="brand-mark" aria-hidden="true"></div>
      <h1 class="brand-name">Heron Fitness</h1>
      <p class="brand-tagline">8 components to a better you</p>
    </header>

    <p class="components-band">Strength, Flexibility, Agility, Core, Power, Balance, Cardiovacular, Speed</p>

    <section class="card-body">
      <h2 class="trainer-name">Mark Delaney</h2>
      <ul class="credentials">
        <li>CQBL Certified Personal Trainer</li>
        <li>CPR AED National Pulse Federation</li>
        <li>B.A. Exercise Physiology W.K.R., 2004</li>
      </ul>

      <ul class="contact-list">
        <li>
          <svg class="contact-icon" viewBox="0 0 28 28" aria-hidden="true">
            <rect x="8" y="3" width="12" height="22" rx="2" fill="none" stroke="var(--brand-red)" stroke-width="2.4"/>
            <rect x="10.5" y="6" width="7" height="7" fill="var(--brand-red)"/>
            <circle cx="14" cy="20" r="1.6" fill="var(--brand-red)"/>
          </svg>
          <span>555-314-2086</span>
        </li>
        <li>
          <svg class="contact-icon" viewBox="0 0 28 28" aria-hidden="true">
            <g fill="none" stroke="var(--brand-red)" stroke-width="2.2">
              <circle cx="14" cy="14" r="11.5"/>
              <ellipse cx="14" cy="14" rx="5" ry="11.5"/>
              <line x1="2.5" y1="14" x2="25.5" y2="14"/>
              <line x1="4.5" y1="8" x2="23.5" y2="8"/>
              <line x1="4.5" y1="20" x2="23.5" y2="20"/>
            </g>
          </svg>
          <span>hernfit4.example</span>
        </li>
        <li>
          <svg class="contact-icon" viewBox="0 0 28 28" aria-hidden="true">
            <rect x="2" y="6" width="24" height="17" rx="1.5" fill="var(--brand-red)"/>
            <polyline points="2.5,7 14,16 25.5,7" fill="none" stroke="var(--card-black)" stroke-width="2"/>
          </svg>
          <span>mark@hernfit4.example</span>
        </li>
      </ul>
    </section>
  </article>
</body>
</html>
```